依頼詳細
コーディング等の作業はございません。載せたい項目・文章関係・動線については添付ラフの内容です。
ビジュアルのみの募集になりますが、もっと良くなりそうなご提案があれば変更してください。

下記の点を求めています。
・コンサル会社のサイトのようなイメージに変えたい!(経験豊富な専任コンサルタントがつき、いろいろアドバイスしてくれるので安心!)(忙しいお客さんや予算と実施のみが決まっているだけで具体的な提案を欲しがっているようなお客さんや納期がなく困っているお客さん等いろんなお客さんからの相談窓口)がほしい。
・自分で探したい人は、色んな用途で探しやすいサイトにしたい。(2軸のコンセプトのサイトを目指しています。)
・イメージカラーは、白ベースに赤

ターゲットは、25~45歳位の企業の販促担当者になります。
男女比は、半々程度です。

下記のようなサイトがいいと思っています。
https://torivane.net/
http://www.kumolo.jp/
サイトURL
http://www.sk-shokai.com/
ページ数
1ページ
希望イメージ
• +5 0 +5
• シンプル
複雑
• 単色
カラフル
• 暗い
明るい
• 日常
高級
• 遊び心
厳粛
• 未来的
伝統的
• 女性的
男性的
希望する色
赤系
納品ファイル
• イラストレーター形式 (.ai)
• フォトショップ形式 (.psd)
補足説明
・メリハリのある見やすいページにしたいです・
・頼りになる販促コンサルタントにおまかせできる(販促コンサルタントのブランディングをしっかりしたい)
・相談したくないもしくは相談前に自分で商品を探してみたい

この3点をしっかり表現出来ているサイトへのリニューアルを目指しています。

よろしくお願いいたします。
依頼公開後の追記内容
プロモエリアのコピーですが、

販促×お悩み相談!=集客商会

で、お願いします。
※もっといいご提案があれば変えていただいても大丈夫です。
必須ではありません。
当社の取扱商品や現在Web上で使用している素材が制作に必要な場合、
下記からダウンロードいただけます。

http://qv7.link/TpAx
パスワード:7wqe

今回の応募作品で制作していただく以外の目的には使用しないように
お願いいたします。
ダウンロード期限:2017年11月9日(木)

より大きいサイズの画像が必要な場合、
同じものをご用意できない可能性もありますが、ご相談くださいませ。
上記サンプルファイルのダウンロード期限が過ぎましたので
再びアップロードいたします。

http://rr828rr.info/K4mb
ダウンロード期限:2017年11月20日(月)

応募の期限は残り僅かですがどうぞよろしくお願いいたします。
■ 選んだ理由

お仕事が丁寧で、デザインもスッキリしていて、且つ訴求ポイントのわかりやすさとのバランスがとても気に入りました。

修正依頼に対するレスもとても早く助かりました。
また、機会がございましたらお願いできたら嬉しいです。
この度は、ありがとうございました。

■ 提案者全員のお礼・コメント

この度は弊社の集客商会のデザインコンペに参加いただき、誠にありがとうございました。
前回、集まりが悪いと思ってしまい途中で取り下げてしまったことが間違いだったと再認識しました。
今回も応募作品のレベルが高く選考するのにかなり迷ってしまいました。
選べなかった作品も素晴い作品が多くありました。
今回ご応募いただいた方々に感謝です。

ありがとうございました。
また、募集の機会がございましたら宜しくお願い致します。

```html
<!DOCTYPE html>
<html lang="ja">
<head>
<meta charset="utf-8">
<title>集客商会</title>
<link href="https://fonts.googleapis.com/css2?family=Noto+Sans+JP:wght@400;500;700;900&family=Montserrat:wght@600;700&display=swap" rel="stylesheet">
<style>
:root{
  --red:#d7222b;
  --red-dark:#b4161f;
  --ink:#333;
  --sub:#777;
  --line:#e2e2e2;
  --pale:#f4f4f4;
  --pink:#f7d9d8;
  --white:#fff;
  --sns-a:#c8386f;
  --sns-b:#3b5a98;
  --sns-c:#35a8e0;
  --sns-d:#d9302b;
}
*{margin:0;padding:0;box-sizing:border-box}
html,body{width:1200px;height:3192px;overflow:hidden}
body{font-family:"Noto Sans JP",sans-serif;color:var(--ink);font-size:12px;background:var(--white);position:relative}
.en{font-family:"Montserrat","Noto Sans JP",sans-serif}
.wrap{width:840px;margin:0 auto;position:relative}
/* header */
.header{height:84px}
.header .wrap{display:flex;align-items:center;height:84px;gap:18px}
.brand{display:flex;align-items:center;gap:8px;font-weight:900;font-size:24px;color:var(--red)}
.brand i{width:30px;height:30px;border-radius:50%;background:var(--red);display:block}
.tagline{font-size:10px;color:var(--sub);line-height:1.6;flex:1}
.tel{text-align:right}
.tel b{font-size:24px;color:var(--red);font-family:"Montserrat",sans-serif;display:flex;align-items:center;gap:6px}
.tel span{font-size:10px;color:var(--sub)}
.gnav{height:40px;border-top:1px solid var(--line);border-bottom:1px solid var(--line)}
.gnav ul{display:flex;list-style:none;height:38px}
.gnav li{flex:1;text-align:center;line-height:38px;font-size:11px;font-weight:500;border-left:1px solid var(--line)}
.gnav li:last-child{border-right:1px solid var(--line)}
.subnav{height:44px;background:var(--pale)}
.subnav .wrap{display:flex;align-items:center;height:44px;gap:26px}
.subnav .item{font-size:10px;font-weight:700;line-height:1.2}
.subnav .item small{display:block;font-weight:400;font-size:8px;color:var(--sub)}
.subnav .search{margin-left:auto;display:flex}
.subnav .search span{width:190px;height:24px;background:#fff;border:1px solid var(--line);font-size:9px;color:#aaa;padding-left:8px;line-height:22px}
.subnav .search b{width:24px;height:24px;background:#555}
/* hero */
.hero{height:328px;display:flex}
.hero-visual{width:600px;position:relative;background:linear-gradient(120deg,#f6dedd,#fbeeee 50%,#efc9c8)}
.hero-visual .photo{position:absolute;left:120px;top:20px;width:240px;height:300px;background:linear-gradient(180deg,#e9c3b4,#f0ded6)}
.hero-copy{position:absolute;left:0;right:0;top:226px;height:46px;background:rgba(215,34,43,.92);color:#fff;font-size:20px;font-weight:700;line-height:46px;padding-left:70px}
.hero-side{flex:1;background:var(--pale);padding:20px 40px}
.panel-title{text-align:center}
.panel-title .en{font-size:9px;color:var(--red);letter-spacing:.1em}
.panel-title h2{font-size:15px;margin:4px 0 8px}
.hero-side p{font-size:9px;line-height:1.7;color:var(--sub);text-align:center}
.btns{display:flex;gap:10px;margin:12px 0 22px}
.btns span{flex:1;height:32px;background:var(--red);color:#fff;font-size:11px;font-weight:700;text-align:center;line-height:32px}
.btns span.alt{background:#fff;color:var(--red);border:1px solid var(--red)}
.selects{display:flex;gap:8px;margin-top:4px}
.selects span{flex:1;height:24px;background:#fff;border:1px solid var(--line);font-size:9px;line-height:22px;padding-left:8px;color:var(--sub)}
.selects b{width:40px;height:24px;background:var(--red)}
.tags{display:flex;gap:5px;margin-top:8px;flex-wrap:wrap}
.tags span{font-size:8px;border:1px solid #ccc;background:#fff;padding:2px 6px}
/* main */
.main{margin-top:30px;height:1250px}
.main .wrap{display:flex;gap:18px}
.side{width:196px}
.side-head{background:var(--red);color:#fff;font-size:11px;font-weight:700;padding:7px 10px}
.side-box{border:1px solid var(--line);padding:8px;margin-bottom:12px}
.side-box span{display:block;height:22px;border:1px solid var(--line)}
.side-list{list-style:none;border:1px solid var(--line);border-top:0;margin-bottom:12px}
.side-list li{font-size:10px;padding:5px 10px 5px 18px;border-bottom:1px dotted var(--line);position:relative}
.side-list li::before{content:"";position:absolute;left:8px;top:10px;width:4px;height:4px;border-right:1px solid var(--red);border-top:1px solid var(--red);transform:rotate(45deg)}
.side-btn{display:block;border:1px solid var(--red);color:var(--red);font-size:10px;font-weight:700;padding:9px 10px;margin-bottom:6px}
.content{flex:1}
.sec-head{display:flex;align-items:baseline;gap:8px;border-bottom:2px solid var(--ink);padding-bottom:5px;margin-bottom:14px}
.sec-head b{font-size:15px}
.sec-head small{font-size:9px;color:var(--sub)}
.feature{display:flex;gap:10px;height:120px;margin-bottom:26px}
.feature .a{width:300px;background:linear-gradient(135deg,#cfd7e2,#eef1f5)}
.feature .b{width:150px;background:linear-gradient(160deg,#2c5aa8,#6f98d6);color:#fff;font-size:14px;font-weight:700;padding:18px 10px}
.feature .c{flex:1;background:linear-gradient(135deg,#e6e6e6,#cfcfcf)}
.points{display:grid;grid-template-columns:1fr 1fr;gap:14px;margin-bottom:26px}
.point{display:flex;gap:10px;height:150px}
.point .img{width:130px;background:linear-gradient(135deg,#d8c4b7,#f0e6df)}
.point:nth-child(2) .img{background:linear-gradient(135deg,#b9cbe0,#e8eef5)}
.point:nth-child(3) .img{background:linear-gradient(135deg,#d9d2c2,#f1ece2)}
.point:nth-child(4) .img{background:linear-gradient(135deg,#9fc1de,#dde9f3)}
.point .txt{flex:1}
.point .num{font-family:"Montserrat",sans-serif;font-size:20px;color:var(--red);font-weight:700}
.point h3{font-size:12px;line-height:1.5;margin:2px 0 6px}
.point p{font-size:9px;color:var(--sub);line-height:1.7}
.achv{display:flex;gap:18px;background:var(--pale);padding:18px;height:300px}
.achv .img{width:250px;background:linear-gradient(135deg,#333,#e8822a 60%,#f2f2f2)}
.achv h3{font-size:15px;line-height:1.7;margin:10px 0 12px}
.achv p{font-size:10px;line-height:1.9;color:var(--sub)}
.dots{display:flex;justify-content:center;align-items:center;gap:8px;margin:16px 0 60px}
.dots i{width:8px;height:8px;border-radius:50%;background:#ccc;display:block}
.dots i.on{background:var(--red)}
.dots b{width:22px;height:22px;border-radius:50%;background:var(--red);display:block}
.news li{list-style:none;display:flex;align-items:center;gap:16px;font-size:10px;padding:16px 0;border-bottom:1px solid var(--line)}
.news .tag{background:var(--red);color:#fff;font-size:9px;padding:2px 10px}
/* banners */
.banners{display:flex;height:140px;margin-top:20px}
.banner{flex:1;background:linear-gradient(135deg,#3a3a3a,#6a6a6a);color:#fff;text-align:center;padding-top:38px}
.banner+.banner{background:linear-gradient(135deg,#2f3b4d,#5c6878)}
.banner b{font-size:20px;display:block}
.banner p{font-size:11px;margin-top:6px}
.banner em{font-style:normal;color:#ff5a5f;font-weight:700}
/* sns */
.sns{display:flex;gap:10px;margin:30px auto 0;width:840px}
.sns div{flex:1;height:66px;color:#fff;text-align:center;padding-top:14px}
.sns b{font-size:15px;display:flex;justify-content:center;align-items:center;gap:8px}
.sns b i{width:12px;height:12px;border-radius:50%;background:rgba(255,255,255,.85);display:block}
.sns small{font-size:8px}
.s1{background:var(--sns-a)}.s2{background:var(--sns-b)}.s3{background:var(--sns-c)}.s4{background:var(--sns-d)}
/* group */
.group{margin-top:34px;text-align:center;height:300px}
.group .en{font-size:13px;font-weight:700}
.group small{display:block;font-size:8px;color:var(--sub);margin-bottom:14px}
.logos{display:grid;grid-template-columns:repeat(4,1fr);gap:12px}
.logos span{height:58px;border:1px solid var(--line);display:flex;align-items:center;justify-content:center;font-weight:700;font-size:14px;color:var(--red)}
/* footer */
.footer{position:absolute;left:0;right:0;top:2410px;bottom:0;background:var(--pale)}
.fcols{display:flex;gap:20px;padding-top:40px}
.fcol{flex:1}
.fcol h4{font-size:10px;margin-bottom:8px}
.fcol li{list-style:none;font-size:9px;color:var(--sub);line-height:2.05}
.copy{position:absolute;bottom:0;left:0;right:0;height:44px;line-height:44px;text-align:center;font-size:9px;color:var(--sub);border-top:1px solid var(--line)}
</style>
</head>
<body>
<header class="header">
  <div class="wrap">
    <div class="brand"><i></i>集客商会</div>
    <div class="tagline">販促のプロが企業の集客を全力でサポート<br>経験豊富な専任コンサルタントが最適なご提案をいたします</div>
    <div class="tel">
      <b><svg width="18" height="18" viewBox="0 0 24 24"><path fill="#d7222b" d="M6.6 10.8a15 15 0 006.6 6.6l2.2-2.2c.3-.3.7-.4 1-.2 1.1.4 2.3.6 3.6.6.6 0 1 .4 1 1V20c0 .6-.4 1-1 1A17 17 0 013 4c0-.6.4-1 1-1h3.5c.6 0 1 .4 1 1 0 1.3.2 2.5.6 3.6.1.3 0 .7-.2 1z"/></svg>0120-418-752</b>
      <span>受付時間 平日9:00〜18:00</span>
    </div>
  </div>
</header>
<nav class="gnav"><div class="wrap"><ul>
  <li>はじめての方へ</li><li>よくある質問</li><li>ご利用の流れ</li><li>お支払い方法</li><li>名入れ方法</li><li>スタッフ紹介</li><li>会社概要</li><li>お問い合わせ</li>
</ul></div></nav>
<div class="subnav"><div class="wrap">
  <div class="item en">CATEGORY<small>カテゴリから探す</small></div>
  <div class="item en">PRICE<small>価格から探す</small></div>
  <div class="item en">EVENT<small>イベントから探す</small></div>
  <div class="item en">TARGET<small>ターゲットから探す</small></div>
  <div class="item en">FEATURE<small>特集から探す</small></div>
  <div class="search"><span>キーワードを入力</span><b></b></div>
</div></div>

<section class="hero">
  <div class="hero-visual">
    <div class="photo" role="img" aria-label="笑顔で相談を受ける女性スタッフの写真"></div>
    <div class="hero-copy">販促×お悩み相談!=集客商会</div>
  </div>
  <div class="hero-side">
    <div class="panel-title"><div class="en">CONTACT</div><h2>相談・お見積もり・お問い合わせ</h2></div>
    <p>専任コンサルタントが予算や納期に合わせて最適な販促品をご提案。<br>急ぎの案件や具体的な企画が決まっていない場合もお気軽にご相談ください。</p>
    <div class="btns"><span>無料で相談する</span><span class="alt">お見積もり依頼</span></div>
    <div class="panel-title"><div class="en">SEARCH</div><h2>キーワード検索</h2></div>
    <div class="selects"><span>商品カテゴリ</span><span>価格帯を選択</span><b></b></div>
    <div class="tags"><span>ボールペン</span><span>タオル</span><span>エコバッグ</span><span>卓上カレンダー</span><span>うちわ</span><span>付箋</span></div>
  </div>
</section>

<main class="main"><div class="wrap">
  <aside class="side">
    <div class="side-head">キーワード検索</div>
    <div class="side-box"><span></span></div>
    <div class="side-head">商品カテゴリ</div>
    <ul class="side-list">
      <li>ファイル・クリアファイル</li><li>文具</li><li>ボールペン</li><li>カレンダー</li><li>タオル</li><li>バッグ・ポーチ</li><li>マグカップ</li><li>ノート・メモ帳</li><li>付箋</li><li>ウェットティッシュ</li><li>うちわ・扇子</li><li>エコグッズ</li><li>キッチン用品</li><li>食品</li><li>傘・雨具</li><li>健康グッズ</li><li>防災用品</li><li>スマホ関連</li><li>アパレル</li><li>ステッカー</li><li>その他</li>
    </ul>
    <span class="side-btn">価格帯から探す</span>
    <span class="side-btn">イベントから探す</span>
    <span class="side-btn">ターゲットから探す</span>
    <span class="side-btn">特集から探す</span>
  </aside>
  <div class="content">
    <div class="sec-head"><b class="en">FEATURE</b><small>特集</small></div>
    <div class="feature">
      <div class="a" role="img" aria-label="販促グッズを並べた特集バナー写真"></div>
      <div class="b">ボールペン特集</div>
      <div class="c" role="img" aria-label="ボールペンの商品写真"></div>
    </div>
    <div class="sec-head"><b class="en">POINT</b><small>集客商会が選ばれる理由</small></div>
    <div class="points">
      <div class="point"><div class="img" role="img" aria-label="打ち合わせの写真"></div><div class="txt"><div class="num">01</div><h3>経験豊富な専任コンサルタントが担当</h3><p>ご予算と目的を伺い、最適な販促品と実施方法を一緒に考えます。</p></div></div>
      <div class="point"><div class="img" role="img" aria-label="電話対応するスタッフの写真"></div><div class="txt"><div class="num">02</div><h3>短納期・お急ぎの案件にも対応</h3><p>納期が迫ったご依頼も、在庫と工場を押さえて迅速に手配します。</p></div></div>
      <div class="point"><div class="img" role="img" aria-label="商品サンプルの写真"></div><div class="txt"><div class="num">03</div><h3>幅広い商品から用途で探せる</h3><p>価格帯やイベント、ターゲット別に豊富な商品を選べます。</p></div></div>
      <div class="point"><div class="img" role="img" aria-label="オフィスで働く人の写真"></div><div class="txt"><div class="num">04</div><h3>企画から効果検証までトータル支援</h3><p>配布後の反応まで見据えた販促プランをご提案いたします。</p></div></div>
    </div>
    <div class="sec-head"><b class="en">ACHIEVEMENT</b><small>実績紹介</small></div>
    <div class="achv">
      <div class="img" role="img" aria-label="実績として紹介する販促品の写真"></div>
      <div><h3>実績として紹介する販促品の名前、もしくは社名の企業名、名前がここに入ります</h3>
      <p>ご依頼の背景や課題、ご提案した内容と配布後の反響などの説明文がここに入ります。ご依頼の背景や課題、ご提案した内容と配布後の反響などの説明文がここに入ります。ご依頼の背景や課題、ご提案した内容の説明文がここに入ります。</p></div>
    </div>
    <div class="dots"><b></b><i class="on"></i><i></i><i></i><i></i><b></b></div>
    <div class="sec-head"><b class="en">NEWS</b><small>お知らせ</small></div>
    <ul class="news">
      <li><span class="en">2017.00.00</span><span class="tag">お知らせ</span>新商品を追加しました。詳しくは商品ページをご覧ください。</li>
      <li><span class="en">2017.00.00</span><span class="tag">お知らせ</span>年末年始の営業日についてのご案内を掲載しました。</li>
      <li><span class="en">2017.00.00</span><span class="tag">お知らせ</span>カレンダー特集ページを公開しました。ぜひご覧ください。</li>
    </ul>
  </div>
</div></main>

<div class="banners">
  <div class="banner" role="img" aria-label="商談中のビジネスシーン写真"><b>即商談!</b><p><em>金額</em>からのお問い合わせはお気軽にお問合せ下さい</p></div>
  <div class="banner" role="img" aria-label="オフィスでの打ち合わせ写真"><b>即商談!</b><p><em>東京23区</em>からのお問い合わせはお気軽にお問合せ下さい</p></div>
</div>

<div class="sns">
  <div class="s1"><b class="en"><i></i>Photogram</b><small>最新情報を配信しています</small></div>
  <div class="s2"><b class="en"><i></i>FaceLink</b><small>最新情報を配信しています</small></div>
  <div class="s3"><b class="en"><i></i>Chirper</b><small>最新情報を配信しています</small></div>
  <div class="s4"><b class="en"><i></i>ViewTube</b><small>最新情報を配信しています</small></div>
</div>

<section class="group wrap">
  <div class="en">GROUP</div><small>集客商会グループ</small>
  <div class="logos">
    <span>プレゼント工房</span><span>あおぎ屋</span><span>しるし工房</span><span>集客商会</span>
    <span>おくりもの屋</span><span>ふせん堂</span><span>こよみ商会</span><span>ふせん堂</span>
    <span>あおぎ屋</span><span>プレゼント工房</span><span>しるし工房</span><span>こよみ商会</span>
  </div>
</section>

<footer class="footer">
  <div class="wrap fcols">
    <div class="fcol"><h4>■ 商品から探す</h4><ul><li>ファイル</li><li>文具</li><li>ボールペン</li><li>カレンダー</li><li>タオル</li><li>バッグ・ポーチ</li><li>マグカップ</li><li>ノート・メモ帳</li><li>付箋</li><li>うちわ・扇子</li><li>エコグッズ</li><li>キッチン用品</li><li>食品</li><li>傘・雨具</li><li>健康グッズ</li><li>防災用品</li><li>スマホ関連</li><li>アパレル</li><li>ステッカー</li><li>その他</li></ul></div>
    <div class="fcol"><h4>■ 価格帯から探す</h4><ul><li>〜50円</li><li>51〜100円</li><li>101〜200円</li><li>201〜300円</li><li>301〜500円</li><li>501〜1000円</li><li>1001〜2000円</li><li>2001〜3000円</li><li>3001円〜</li></ul></div>
    <div class="fcol"><h4>■ 行事・イベントで探す</h4><ul><li>展示会・見本市</li><li>新年・年末</li><li>春の行事</li><li>夏の行事</li><li>秋の行事</li><li>周年記念</li><li>キャンペーン</li><li>オープン記念</li><li>セミナー</li><li>採用活動</li><li>株主総会</li><li>スポーツ大会</li></ul></div>
    <div class="fcol"><h4>■ ターゲットで探す</h4><ul><li>男性向け</li><li>女性向け</li><li>子ども向け</li><li>シニア向け</li><li>学生向け</li><li>ビジネス向け</li><li>ファミリー向け</li></ul></div>
    <div class="fcol"><h4>■ 特集から探す</h4><ul><li>ボールペン特集</li><li>カレンダー特集</li><li>タオル特集</li><li>エコ特集</li><li>防災特集</li><li>食品特集</li><li>名入れ特集</li><li>短納期特集</li></ul></div>
  </div>
  <div class="copy">Copyright © 集客商会 All Rights Reserved.</div>
</footer>
</body>
</html>
```